Band Autograph Postcard

We are Velvet Hollow a classically influenced - Gothic alternative - Progressive Rock band looking to have a postcard designed for us to mail out for autographs.

We would like to design this with our photos and have a layout that we can all sign underneath our pictures. Please create a design using the photos attached and we need this to be one cohesive design. We would also like to include our logo.

You can cut out the photos to fit your design needs.

Please incorporate the following into this design:

1. Band name (Velvet Hollow) Ringbearer Font on the front
2. website: www.VelvetHollowSound.example on the front
3. Photos & Logo
4. Our links on the back of the postcard
www.friendspage.example/VelvetHollowSound
www.bandloft.example/VelvetHollow
Follow us on chirpline @VelvetHollowSound

5. A space to add mailing address
6. Dark colored tones

This postcard needs to be laid out for an oversized postcard we will be using printmerle.example for our printing so please check the sizes.  We will be signing them so they will need to be able to read our signatures and not have the card be too black or too dark.

I uploaded a photo to show the layout.

```html
<!DOCTYPE html>
<html lang="en">
<head>
<meta charset="utf-8">
<title>Velvet Hollow — Autograph Postcard Back</title>
<link rel="stylesheet" href="https://fonts.googleapis.com/css2?family=Cinzel:wght@400;600;700&display=swap">
<style>
  :root {
    --paper: #ffffff;
    --stamp-grey: #a9a9a9;
    --ribbon-brown: #7a5a1e;
    --rule-brown: #7f5e22;
    --wordmark-tan: #b9ab8c;
    --link-brown: #4a3412;
    --mark-tone: #8c8378;
  }
  html, body {
    margin: 0;
    padding: 0;
    overflow: hidden;
    background: var(--paper);
  }
  .postcard-back {
    position: relative;
    width: 1200px;
    height: 929px;
    background: var(--paper);
    overflow: hidden;
  }
  .stamp-label {
    position: absolute;
    left: 900px;
    top: 84px;
    width: 112px;
    text-align: center;
    font-family: "Cinzel", serif;
    font-size: 29px;
    color: var(--stamp-grey);
    letter-spacing: 1px;
  }
  .band-mark-square {
    position: absolute;
    left: 176px;
    top: 380px;
    width: 240px;
    height: 240px;
    background: var(--mark-tone);
  }
  .band-wordmark {
    position: absolute;
    left: 60px;
    top: 668px;
    width: 470px;
    text-align: center;
    font-family: "Cinzel", serif;
    font-weight: 400;
    font-size: 52px;
    line-height: 64px;
    color: var(--wordmark-tan);
    white-space: nowrap;
  }
  .band-links {
    position: absolute;
    left: 0;
    top: 774px;
    width: 1200px;
    margin: 0;
    padding: 0;
    list-style: none;
    text-align: center;
    font-family: "Cinzel", serif;
    font-weight: 600;
    font-size: 21px;
    line-height: 29px;
    color: var(--link-brown);
  }
  .recipient-ribbon {
    position: absolute;
    left: 680px;
    top: 292px;
  }
  .address-lines {
    position: absolute;
    left: 621px;
    top: 460px;
    width: 472px;
    margin: 0;
    padding: 0;
    list-style: none;
  }
  .address-lines li {
    height: 6px;
    background: var(--rule-brown);
    margin-bottom: 48px;
  }
</style>
</head>
<body>
  <main class="postcard-back">
    <div class="stamp-label">STAMP</div>

    <div class="band-mark-square" aria-hidden="true"></div>
    <div class="band-wordmark">Velvet Hollow</div>

    <ul class="band-links">
      <li>www.bandloft.example/VelvetHollow</li>
      <li>www.friendspage.example/VelvetHollowSound</li>
      <li>Follow us on chirpline @VelvetHollowSound</li>
    </ul>

    <section aria-label="Mailing address">
      <svg class="recipient-ribbon" width="370" height="62" viewBox="0 0 370 62">
        <path d="M0 54 Q20 32 18 8 Q185 -4 352 8 Q350 32 370 54 Q185 38 0 54 Z" fill="var(--ribbon-brown)"/>
        <text x="185" y="39" text-anchor="middle" font-family="Cinzel, serif" font-weight="600" font-size="25" fill="#ffffff">Recipient</text>
      </svg>
      <ul class="address-lines">
        <li></li>
        <li></li>
        <li></li>
        <li></li>
      </ul>
    </section>
  </main>
</body>
</html>
```